Tivelle shoes is a wholesale shoe sales company , mostly working in female shoes and kiddies shoes with a small mens section . looking for a clean slick look. http://www.brindafeet.co.za/shop/ is a good reference

It Company

```html
<!DOCTYPE html>
<html lang="en">
<head>
<meta charset="utf-8">
<title>Tivelle Shoes</title>
<link rel="stylesheet" href="https://fonts.googleapis.com/css2?family=Varela+Round&family=Open+Sans:wght@400;600;700&display=swap">
<style>
:root{
  --ink:#3a3a3a;
  --muted:#6d6d6d;
  --soft:#9a9a9a;
  --accent:#e4531f;
  --topbar:#262626;
  --line:#e3e3e3;
  --band:#ebebea;
  --base:#f5f5f4;
  --blue:#2f8fdb;
  --white:#fff;
}
*{box-sizing:border-box;margin:0;padding:0}
html,body{width:672px;height:1200px;overflow:hidden;background:var(--white)}
body{position:relative;font-family:"Open Sans",Arial,sans-serif;color:var(--ink)}
.abs{position:absolute}
.topbar{left:0;top:0;width:672px;height:47px;background:var(--topbar);color:#ddd;font-size:9px}
.topbar .account{left:48px;top:19px}
.topbar .cart{right:52px;top:19px;display:flex;align-items:center;gap:5px}
.header{left:47px;top:47px;width:572px;height:68px;border-bottom:1px solid var(--line)}
.logo{left:0;top:18px;font-family:"Varela Round",sans-serif;font-size:25px;color:var(--accent)}
.nav{right:0;top:0;display:flex;height:67px}
.nav-item{text-align:center;padding-top:23px;font-size:8.5px;text-transform:uppercase;color:var(--ink);width:66px}
.nav-item small{display:block;text-transform:none;font-style:italic;font-size:7px;color:var(--soft);margin-top:4px}
.nav-item.active{background:#f2f2f2;border-top:3px solid var(--accent);padding-top:20px}
.tagline{left:0;top:137px;width:672px;text-align:center;font-family:"Varela Round",sans-serif;font-size:15.5px;line-height:24px;color:var(--muted)}
.hero{left:47px;top:203px;width:572px;height:288px;background:linear-gradient(135deg,#f3f3f1,#e6e6e3 55%,#d9dadb)}
.hero-arrows{left:62px;top:451px}
.tabs{left:47px;top:491px;width:572px;height:53px;display:flex;background:#f4f4f4}
.tab{flex:1;display:flex;align-items:center;padding-left:10px;gap:22px;border-bottom:1px solid var(--line)}
.tab.active{background:#ebebeb;border-top:2px solid var(--accent)}
.tab-num{width:28px;height:28px;border-radius:50%;background:var(--accent);color:#fff;font-weight:700;font-size:14px;display:flex;align-items:center;justify-content:center}
.tab-title{font-size:14px;color:#222}
.tab.active .tab-title{color:var(--accent)}
.tab-sub{font-size:8px;color:var(--muted);margin-top:2px}
.section-title{left:0;top:567px;width:672px;text-align:center;font-family:"Varela Round",sans-serif;font-size:16px;font-weight:400}
.product{top:605px;width:124px;height:157px;border:1px solid var(--line);text-align:center}
.product .shot{margin:18px auto 0;width:92px;height:64px;border-radius:4px}
.product .name{font-size:8px;color:var(--muted);margin-top:15px;text-transform:uppercase}
.product .price{font-size:9px;font-weight:700;margin-top:6px}
.product .stars{font-size:8px;color:#aaa;letter-spacing:1px;margin-top:5px}
.links{left:0;top:799px;width:672px;height:228px;background:var(--band)}
.col{top:823px;font-size:8px;color:var(--muted);line-height:18px}
.col h3{font-weight:400;font-size:12px;color:var(--ink);margin-bottom:6px}
.col h3.spacer{visibility:hidden}
.base{left:0;top:1027px;width:672px;height:173px;background:var(--base)}
.block{top:1050px}
.block h4{font-weight:400;font-size:10px;text-transform:uppercase;color:var(--ink);margin-bottom:9px}
.block p{font-size:7.5px;line-height:14px;color:var(--muted)}
.signup{left:47px;width:210px}
.field{width:124px;height:22px;background:#fff;border:1px solid #ccc;display:inline-block;vertical-align:top;margin-top:12px}
.btn{display:inline-block;background:var(--blue);color:#fff;font-size:9px;height:22px;line-height:22px;padding:0 14px;margin-top:12px;margin-left:4px}
.accept{left:290px}
.cards{display:flex;gap:14px;align-items:center;font-size:8.5px;color:var(--muted);margin-top:2px}
.badges{display:flex;gap:18px;margin-top:18px}
.badge{width:40px;height:20px;border-radius:4px;background:#dcdfe6}
.badge.round{width:42px;border-radius:10px;background:#e3d5d7}
.touch{left:488px;width:136px}
.social{display:flex;gap:6px;margin-top:10px}
.social span{width:18px;height:18px}
.copy{left:47px;top:1155px;width:572px;border-top:1px solid var(--line);padding-top:14px;font-size:7.5px;color:var(--ink)}
</style>
</head>
<body>
<div class="abs topbar">
  <div class="abs account">Register &nbsp;|&nbsp; Login &nbsp;|&nbsp; My Account</div>
  <div class="abs cart"><svg width="11" height="10" viewBox="0 0 11 10"><path d="M0 1h2l2 6h6l1-4H3" fill="none" stroke="#e4531f" stroke-width="1.3"/><circle cx="5" cy="9" r="1" fill="#e4531f"/><circle cx="9" cy="9" r="1" fill="#e4531f"/></svg>Cart (0) items</div>
</div>

<header class="abs header">
  <div class="abs logo">Tivelle Shoes</div>
  <nav class="abs nav">
    <div class="nav-item active">Home<small>all starts here</small></div>
    <div class="nav-item" style="width:69px">About us<small>adipiscing</small></div>
    <div class="nav-item" style="width:60px">Men<small>Aenean masa</small></div>
    <div class="nav-item" style="width:82px">Ladies &amp; Kids<small>commodo ligula</small></div>
    <div class="nav-item" style="width:80px">Contact<small>sit amet</small></div>
  </nav>
</header>

<p class="abs tagline">Aenean commodo ligula eget dolor. Aenean massa.<br>Lorem ipsum dolor sit amet nec, consectetuer adipiscing elit.</p>

<div class="abs hero" role="img" aria-label="Photo of two casual sneakers, navy and grey, on a white wooden floor"></div>
<svg class="abs hero-arrows" width="38" height="26" viewBox="0 0 38 26"><path d="M12 1L2 13l10 12M24 1l10 12-10 12" fill="none" stroke="#fff" stroke-width="1.5"/></svg>

<div class="abs tabs">
  <div class="tab"><div class="tab-num">1</div><div><div class="tab-title">Female Shoes</div><div class="tab-sub">Lorem ipsum dolor sit amet</div></div></div>
  <div class="tab active"><div class="tab-num">2</div><div><div class="tab-title">Men's Shoes</div><div class="tab-sub">Lorem ipsum dolor sit amet</div></div></div>
  <div class="tab"><div class="tab-num">3</div><div><div class="tab-title">Kiddies Shoes</div><div class="tab-sub">Lorem ipsum dolor sit amet</div></div></div>
</div>

<h2 class="abs section-title">New Arrivals</h2>

<div class="abs product" style="left:47px"><div class="shot" role="img" aria-label="Photo of a grey slip-on shoe" style="background:linear-gradient(135deg,#8a93a6,#4b5568)"></div><div class="name">Combined Jacket</div><div class="price">$119.50</div><div class="stars">☆☆☆☆☆</div></div>
<div class="abs product" style="left:197px"><div class="shot" role="img" aria-label="Photo of a black polka-dot high heel" style="background:linear-gradient(135deg,#3a3a3a,#111)"></div><div class="name">Combined Jacket</div><div class="price">$119.50</div><div class="stars">☆☆☆☆☆</div></div>
<div class="abs product" style="left:346px"><div class="shot" role="img" aria-label="Photo of a patterned sneaker with red laces" style="background:linear-gradient(135deg,#5a5a5a,#c9485a)"></div><div class="name">Combined Jacket</div><div class="price">$119.50</div><div class="stars">☆☆☆☆☆</div></div>
<div class="abs product" style="left:495px"><div class="shot" role="img" aria-label="Photo of a red and cream running shoe" style="background:linear-gradient(135deg,#d9443a,#e8d6b8)"></div><div class="name">Combined Jacket</div><div class="price">$119.50</div><div class="stars">☆☆☆☆☆</div></div>

<section class="abs links"></section>
<div class="abs col" style="left:47px"><h3>Woman</h3>Lorem ipsum<br>Aenean massa<br>Adipiscing elit<br>Recreational<br>Interdum sit amet<br>Natoque penatibus<br>Commodo ligula<br>Nsectetuer adipiscing</div>
<div class="abs col" style="left:174px"><h3 class="spacer">Woman</h3>Lorem ipsum<br>Aenean massa<br>Adipiscing elit<br>Recreational<br>Interdum sit amet<br>Natoque penatibus<br>Commodo ligula<br>Nsectetuer adipiscing</div>
<div class="abs col" style="left:301px"><h3 class="spacer">Woman</h3>Lorem ipsum<br>Aenean massa<br>Adipiscing elit<br>Recreational</div>
<div class="abs col" style="left:401px"><h3>Men</h3>Lorem ipsum<br>Aenean massa<br>Adipiscing elit<br>Recreational<br>Interdum sit amet<br>Natoque penatibus<br>Commodo ligula<br>Nsectetuer adipiscing</div>
<div class="abs col" style="left:535px"><h3>Brands</h3>Lorem ipsum<br>Aenean massa<br>Adipiscing elit<br>Recreational<br>Interdum sit amet<br>Natoque penatibus<br>Commodo ligula<br>Nsectetuer adipiscing</div>

<footer class="abs base"></footer>
<div class="abs block signup"><h4>Newsletter Signup</h4><p>Stay in touch with us by signing up for our<br>quarterly newsletter!</p><span class="field"></span><span class="btn">SUBSCRIBE</span></div>
<div class="abs block accept"><h4>We Accept</h4>
  <div class="cards"><span>Corvan</span><span>Halden</span><span>Brisk</span><span>Tallow</span></div>
  <div class="badges"><span class="badge"></span><span class="badge round"></span></div>
</div>
<div class="abs block touch"><h4>Get in Touch</h4><p>Follow our news and events through social network get our free updates.</p>
  <div class="social"><span style="background:#3b5998"></span><span style="background:#2fa9e0"></span><span style="background:#f26b22"></span></div>
</div>
<div class="abs copy">Copyright © 2013. All Rights Reserved.</div>
</body>
</html>
```